We need a design for a clothing tag for our summer hats & sandals line. Tag should be 2.25" high by 2" wide with a little hole punch circle in the top center. The brand is "Coral Drift" so it should have that name on the tag & then I would also like "Summer Apparel" on the tag somewhere lower on the tag perhaps in a bit smaller font. It should obviously be summer themed- with a picture of a beach or sand- something to that effect. Our previous brand was "Lumen Days"- I have attached that artwork so you can get an idea of what we are looking for.

Logo Text

Coral Drift

```html
<!DOCTYPE html>
<html lang="en">
<head>
<meta charset="utf-8">
<title>Coral Drift – Summer Apparel Tag</title>
<link rel="stylesheet" href="https://fonts.googleapis.com/css2?family=Cinzel:wght@500&display=swap">
<style>
  :root {
    --sky-top: #7fa6d4;
    --sky-low: #b2c9de;
    --sand-light: #f4d2ca;
    --sand-wet: #e8988a;
    --surf: #d7efe9;
    --lagoon: #45c6cf;
    --deep-sea: #1a86c0;
    --brand-navy: #2e3190;
    --ink: #1b1512;
    --punch: #ffffff;
    --page: #ffffff;
  }
  html, body {
    margin: 0;
    padding: 0;
    width: 1067px;
    height: 1200px;
    overflow: hidden;
    background: var(--page);
  }
  .tag {
    position: relative;
    width: 1067px;
    height: 1200px;
    overflow: hidden;
  }
  .beach-scene {
    position: absolute;
    inset: 0;
    background:
      linear-gradient(180deg, var(--sky-top) 0%, var(--sky-low) 20%, transparent 20.5%),
      linear-gradient(118deg,
        var(--sand-light) 0%,
        var(--sand-light) 38%,
        var(--sand-wet) 47%,
        var(--surf) 53%,
        var(--lagoon) 64%,
        var(--deep-sea) 100%);
  }
  .hole-punch {
    position: absolute;
    left: 495px;
    top: 92px;
    width: 74px;
    height: 74px;
    border-radius: 50%;
    background: var(--punch);
  }
  .brand-name {
    position: absolute;
    left: 0;
    right: 0;
    top: 340px;
    margin: 0;
    text-align: center;
    font-family: "Cinzel", serif;
    font-weight: 500;
    font-size: 190px;
    line-height: 1.3;
    letter-spacing: 0.04em;
    color: var(--brand-navy);
  }
  .brand-name span {
    display: block;
  }
  .tagline {
    position: absolute;
    left: 0;
    right: 0;
    top: 1062px;
    margin: 0;
    text-align: center;
    font-family: "Cinzel", serif;
    font-weight: 500;
    font-size: 78px;
    letter-spacing: 0.16em;
    color: var(--ink);
    line-height: 1;
  }
</style>
</head>
<body>
  <div class="tag">
    <div class="beach-scene" role="img" aria-label="Aerial photo of a pink sand beach curving along turquoise sea under a blue sky, with green trees along the shore"></div>
    <div class="hole-punch"></div>
    <h1 class="brand-name">
      <span>Coral</span>
      <span>Drift</span>
    </h1>
    <p class="tagline">Summer Apparel</p>
  </div>
</body>
</html>
```